DrBrambo flyer design

I'd like a simple flyer design for my self serve frozen yogurt buffet. It needs to be clear and easy to read without getting bored. I'd like a clean simple design for a double page A5 flyer. I really like the flyer examples i have attached. Something like these would be good. Thankyou. The name of our shop is Dr. Brambo. We are the first self serve frozen yogurt shop in Thailand. Edit: Just to confirm, we're not offering a 50% discount. I would like something similsr to the examples.

```html
<!DOCTYPE html>
<html lang="en">
<head>
<meta charset="utf-8">
<title>Dr. Brambo – Now Open Flyer</title>
<link rel="stylesheet" href="https://fonts.googleapis.com/css2?family=Archivo+Black&family=Rammetto+One&family=Titan+One&display=swap">
<style>
  :root {
    --white: #ffffff;
    --ink: #1a1a1a;
    --lime: #a8f01c;
    --pink: #f29ac0;
    --magenta: #e8157d;
    --yellow: #fff200;
    --sky: #4fd6f2;
    --red: #ee2a3a;
    --berry: #c8325f;
    --berry-light: #f3c4d2;
  }
  * { box-sizing: border-box; margin: 0; padding: 0; }
  html, body { width: 846px; height: 1200px; overflow: hidden; background: var(--white); }
  .flyer {
    position: relative;
    width: 846px;
    height: 1200px;
    overflow: hidden;
    background: var(--white);
    font-family: "Archivo Black", sans-serif;
  }

  /* brand */
  .brand {
    position: absolute;
    left: 0; top: 60px;
    width: 846px; height: 260px;
    display: flex; align-items: center; justify-content: center; gap: 26px;
  }
  .brand-dot { width: 70px; height: 70px; border-radius: 50%; background: var(--lime); }
  .brand-name {
    font-family: "Archivo Black", sans-serif;
    font-size: 118px; line-height: 1;
    color: var(--lime); letter-spacing: -2px;
  }

  /* product photo */
  .product-photo {
    position: absolute;
    left: 0; top: 371px;
    width: 320px; height: 580px;
    background: radial-gradient(ellipse at 40% 30%, var(--berry-light) 0%, var(--berry) 45%, #e9e4e6 80%, #f7f7f7 100%);
    border-radius: 0 60% 0 0 / 0 20% 0 0;
  }

  .frames { position: absolute; left: 0; top: 0; width: 846px; height: 1200px; }

  .outlined {
    text-shadow:
      -2px -2px 0 var(--ink), 2px -2px 0 var(--ink),
      -2px 2px 0 var(--ink), 2px 2px 0 var(--ink),
      0 -2px 0 var(--ink), 0 2px 0 var(--ink),
      -2px 0 0 var(--ink), 2px 0 0 var(--ink);
  }

  /* opening banner */
  .opening {
    position: absolute;
    left: 132px; top: 418px;
    width: 648px; height: 151px;
    text-align: center;
  }
  .opening-tagline {
    margin-top: 30px; margin-left: 30px;
    font-size: 20px; color: var(--white); letter-spacing: 0.3px;
  }
  .opening-headline {
    margin-top: 4px; margin-left: 40px;
    font-family: "Rammetto One", serif;
    font-size: 52px; letter-spacing: 7px; line-height: 1.1;
    white-space: nowrap;
  }
  .c-sky { color: var(--sky); }
  .c-red { color: var(--red); }
  .c-yellow { color: var(--yellow); }

  /* steps */
  .step {
    position: absolute;
    display: flex; flex-direction: column; align-items: center; justify-content: center;
    text-align: center;
  }
  .step-number { font-family: "Titan One", sans-serif; line-height: 1; }
  .step-label { color: var(--white); line-height: 1; white-space: nowrap; }

  .step-one { left: 207px; top: 545px; width: 160px; height: 160px; }
  .step-one .step-number { font-size: 56px; color: var(--sky); }
  .step-one .step-label { font-size: 20px; margin-top: 6px; }

  .step-two { left: 310px; top: 682px; width: 236px; height: 236px; }
  .step-two .step-number { font-size: 92px; color: var(--magenta); }
  .step-two .step-label { font-size: 30px; margin-top: 8px; }

  .step-three { left: 0; top: 870px; width: 345px; height: 300px; }
  .step-three .step-number { font-size: 100px; color: var(--yellow); }
  .step-three .step-label { font-size: 31px; margin-top: 10px; }
  .step-three .step-accent {
    font-family: "Rammetto One", serif;
    font-size: 56px; letter-spacing: 5px;
    color: var(--lime); margin-top: 4px; line-height: 1;
  }

  /* visit info */
  .visit {
    position: absolute;
    right: 36px; top: 682px;
    text-align: right;
  }
  .visit-heading { font-size: 25px; color: var(--magenta); line-height: 1.1; }
  .visit-value { font-family: "Titan One", sans-serif; color: var(--yellow); line-height: 1; }
  .visit-address { display: flex; align-items: center; justify-content: flex-end; gap: 4px; margin-bottom: 46px; }
  .visit-address .visit-value { font-size: 56px; }
  .visit-street { font-size: 22px; color: var(--yellow); line-height: 0.95; text-align: left; }
  .visit-hours { font-size: 50px; margin-bottom: 40px; }
  .visit-phone { font-size: 37px; letter-spacing: 2px; white-space: nowrap; }

  /* slogan banner */
  .slogan {
    position: absolute;
    left: 357px; top: 1029px;
    width: 489px; height: 132px;
    display: flex; flex-direction: column; align-items: flex-end; justify-content: center;
    padding-right: 46px;
  }
  .slogan-title {
    font-family: "Rammetto One", serif;
    font-size: 44px; letter-spacing: 5px;
    color: var(--magenta); line-height: 1.1;
  }
  .slogan-note { font-size: 23px; color: var(--white); margin-top: 4px; }
</style>
</head>
<body>
<main class="flyer">

  <header class="brand">
    <span class="brand-dot"></span>
    <h1 class="brand-name">Dr. Brambo</h1>
  </header>

  <div class="product-photo" role="img" aria-label="Photo of a cup of swirled berry frozen yogurt topped with colourful candy pieces"></div>

  <svg class="frames" viewBox="0 0 846 1200" aria-hidden="true">
    <rect x="139" y="425" width="634" height="137" fill="var(--pink)" stroke="var(--yellow)" stroke-width="14"/>
    <rect x="139" y="425" width="634" height="137" fill="none" stroke="var(--magenta)" stroke-width="7" stroke-linecap="round" stroke-dasharray="0 19"/>
    <rect x="364" y="1036" width="500" height="118" fill="var(--pink)" stroke="var(--yellow)" stroke-width="14"/>
    <rect x="364" y="1036" width="500" height="118" fill="none" stroke="var(--magenta)" stroke-width="7" stroke-linecap="round" stroke-dasharray="0 19"/>
    <circle cx="287" cy="625" r="76" fill="var(--white)" stroke="var(--yellow)" stroke-width="12"/>
    <circle cx="287" cy="625" r="76" fill="none" stroke="var(--magenta)" stroke-width="7" stroke-linecap="round" stroke-dasharray="0 19"/>
    <circle cx="428" cy="800" r="114" fill="var(--white)" stroke="var(--yellow)" stroke-width="12"/>
    <circle cx="428" cy="800" r="114" fill="none" stroke="var(--magenta)" stroke-width="7" stroke-linecap="round" stroke-dasharray="0 19"/>
    <circle cx="172" cy="1022" r="174" fill="var(--white)" stroke="var(--yellow)" stroke-width="12"/>
    <circle cx="172" cy="1022" r="174" fill="none" stroke="var(--magenta)" stroke-width="7" stroke-linecap="round" stroke-dasharray="0 19"/>
  </svg>

  <section class="opening">
    <p class="opening-tagline outlined">1ST FROZEN YOGURT BUFFET IN THAILAND</p>
    <p class="opening-headline outlined"><span class="c-sky">NOW</span> <span class="c-red">OPE</span><span class="c-yellow">N!</span></p>
  </section>

  <div class="step step-one">
    <span class="step-number outlined">1</span>
    <span class="step-label outlined">YOGURT</span>
  </div>
  <div class="step step-two">
    <span class="step-number outlined">2</span>
    <span class="step-label outlined">TOPPINGS</span>
  </div>
  <div class="step step-three">
    <span class="step-number outlined">3</span>
    <span class="step-label outlined">WEIGH, PAY &amp;</span>
    <span class="step-accent outlined">ENJOY</span>
  </div>

  <section class="visit">
    <p class="visit-heading outlined">FIND US AT</p>
    <div class="visit-address">
      <span class="visit-value outlined">150</span>
      <span class="visit-street outlined">STREET<br>CITY</span>
    </div>
    <p class="visit-heading outlined">HOURS</p>
    <p class="visit-value visit-hours outlined">9-5</p>
    <p class="visit-heading outlined">CALL AHEAD</p>
    <p class="visit-value visit-phone outlined">(555) 555-5555</p>
  </section>

  <section class="slogan">
    <p class="slogan-title outlined">"SLOGAN"</p>
    <p class="slogan-note outlined">INSERT HERE</p>
  </section>

</main>
</body>
</html>
```